Brenner Business Cards

Front of business card will have logo, name, address, & telephone number. Back of card will have a list of services provided - Roads, Substation Pads, Temporary Pads, Site Pads, Land Leveling, Powerline Row Cleaning, Land Clearing, Gates, Fencing, Construction Entrances, Excavation, Trenching, Underground Utilities, Directional Boring, Pile Driving. We are a construction company that uses heavy equipment like bulldozers, motor graders/blades, dump trucks, backhoes, hydro axes, & skid loaders. We build roads, pads, & install electric utility lines & waterlines underground. This logo is new. The word "Construction" can be smaller as uploaded 2 example edited logos. We will be using this card design for many employees.
Target Market(s)
Industrial Electric Powerline, Wind Turbine, Solar Panel, & Water Utility companies.
Contact Information for Business Card
Name/Position - Danny Brenner - Owner
Address: 4837 FM 952
Cedar Bluff, TX 79284
Phone number - (325) 518-2906

```html
<!DOCTYPE html>
<html lang="en">
<head>
<meta charset="utf-8">
<title>Brenner Construction Business Cards</title>
<link rel="stylesheet" href="https://fonts.googleapis.com/css2?family=Lato:wght@400;700&display=swap">
<style>
  :root {
    --maroon: #3a111b;
    --white: #ffffff;
    --page: #5b5b5b;
    --edge-grey: #7a7a7a;
  }
  * { box-sizing: border-box; margin: 0; padding: 0; }
  html, body { width: 1200px; height: 900px; overflow: hidden; }
  body {
    background: var(--page);
    font-family: "Lato", sans-serif;
    position: relative;
  }
  .card {
    position: absolute;
    left: 320px;
    width: 560px;
    height: 320px;
    border-radius: 16px;
    overflow: hidden;
    background: var(--maroon);
    color: var(--white);
  }
  .card--front { top: 110px; }
  .card--back { top: 470px; }

  .front-shape { position: absolute; inset: 0; }

  .contact { position: absolute; left: 34px; top: 34px; width: 220px; }
  .contact__name { font-weight: 700; font-size: 26px; line-height: 1.1; }
  .contact__role { font-size: 15px; margin-top: 2px; }
  .contact__rule { width: 22px; height: 1px; background: var(--white); margin: 22px 0 20px; }
  .contact__address { font-size: 15px; line-height: 1.3; margin-bottom: 6px; }
  .contact__line { display: flex; align-items: center; gap: 8px; font-size: 14.5px; line-height: 1.5; white-space: nowrap; }
  .contact__line svg { width: 12px; height: 12px; flex: none; }

  .wordmark { position: absolute; display: flex; align-items: center; gap: 10px; text-transform: uppercase; font-weight: 400; letter-spacing: 1px; line-height: 1; }
  .wordmark__square { width: 20px; height: 20px; flex: none; }
  .wordmark__text { display: flex; flex-direction: column; align-items: flex-start; }
  .wordmark__name { font-size: 30px; }
  .wordmark__sub { font-size: 20px; margin-top: 4px; }

  .card--front .wordmark { left: 326px; top: 138px; color: var(--maroon); }
  .card--front .wordmark__square { background: var(--maroon); }
  .card--back .wordmark { left: 200px; top: 30px; color: var(--white); }
  .card--back .wordmark__square { background: var(--white); }

  .services-title { position: absolute; left: 0; right: 0; top: 140px; text-align: center; font-weight: 700; font-size: 22px; letter-spacing: .5px; }
  .services { position: absolute; list-style: none; font-size: 13px; line-height: 1.3; }
  .services li { display: flex; align-items: center; gap: 8px; }
  .services li::before { content: ""; width: 5px; height: 5px; border-radius: 50%; background: var(--white); flex: none; }
  .services--left { left: 32px; top: 102px; }
  .services--right { right: 32px; top: 180px; text-align: right; }
  .services--right li { flex-direction: row-reverse; }
</style>
</head>
<body>

<section class="card card--front" aria-label="Business card front">
  <svg class="front-shape" viewBox="0 0 560 320" preserveAspectRatio="none" aria-hidden="true">
    <path d="M248 320 C 250 200 330 70 560 40 L560 320 Z" fill="var(--edge-grey)"/>
    <path d="M262 320 C 264 205 340 80 560 52 L560 320 Z" fill="var(--white)"/>
  </svg>

  <div class="contact">
    <p class="contact__name">Danny Brenner</p>
    <p class="contact__role">Owner</p>
    <div class="contact__rule"></div>
    <p class="contact__address">4837 FM 952<br>Cedar Bluff, TX 79284</p>
    <p class="contact__line">
      <svg viewBox="0 0 12 12"><path d="M2.5 1 L4.5 1 L5.3 3.5 L4 4.5 C4.6 6 6 7.4 7.5 8 L8.5 6.7 L11 7.5 L11 9.5 C11 10.3 10.3 11 9.5 11 C5 11 1 7 1 2.5 C1 1.7 1.7 1 2.5 1 Z" fill="var(--white)"/></svg>
      (325) 518-2906
    </p>
    <p class="contact__line">
      <svg viewBox="0 0 12 12"><rect x="1" y="2.5" width="10" height="7" fill="none" stroke="var(--white)" stroke-width="1.2"/><path d="M1 2.5 L6 6.5 L11 2.5" fill="none" stroke="var(--white)" stroke-width="1.2"/></svg>
      info@brennerconstruction.com
    </p>
    <p class="contact__line">
      <svg viewBox="0 0 12 12"><circle cx="6" cy="6" r="5" fill="none" stroke="var(--white)" stroke-width="1.1"/><ellipse cx="6" cy="6" rx="2.2" ry="5" fill="none" stroke="var(--white)" stroke-width="1"/><path d="M1 6 H11" stroke="var(--white)" stroke-width="1"/></svg>
      www.brennerconstruction.com
    </p>
  </div>

  <div class="wordmark">
    <span class="wordmark__square"></span>
    <span class="wordmark__text">
      <span class="wordmark__name">Brenner</span>
      <span class="wordmark__sub">Construction</span>
    </span>
  </div>
</section>

<section class="card card--back" aria-label="Business card back">
  <div class="wordmark">
    <span class="wordmark__square"></span>
    <span class="wordmark__text">
      <span class="wordmark__name">Brenner</span>
      <span class="wordmark__sub">Construction</span>
    </span>
  </div>

  <ul class="services services--left">
    <li>Roads</li>
    <li>Substation Pads</li>
    <li>Temporary Pads</li>
    <li>Site Pads</li>
    <li>Land Leveling</li>
    <li>Powerline Row Cleaning</li>
    <li>Land Clearing</li>
    <li>Gates</li>
  </ul>

  <h2 class="services-title">SERVICES</h2>

  <ul class="services services--right">
    <li>Fencing</li>
    <li>Construction Entrances</li>
    <li>Excavation</li>
    <li>Trenching</li>
    <li>Underground Utilities</li>
    <li>Directional Boring</li>
    <li>Pile Driving</li>
  </ul>
</section>

</body>
</html>
```